Design a business card & stationary for a mortgage company

We are looking for a good looking business card design for our mortgage company that includes our logo. We received a free design as part of our logo project but we don't love it. The company is called "Pinecrest Mortgage Company" so we like waves and lighthouses. The logo should be included. We have a version in both vertical and horizontal that we have provided.

Industry/Entity Type

Finance

Contact Information for Business Card

This should include our new logo file

Requirements
Must have
• 3. The details you'd like on the card - name, title, phone, email, website, address, social media handles etc.
1. Marcus Hale
Vice President
555-419-6253
Fax 888-304-2918
mhale@pinecrestmortgage.example
NMLS 47162 - Company NMLS 61290
18 Larkin Ave
Seabrook Bay, SB 08614

```html
<!DOCTYPE html>
<html lang="en">
<head>
<meta charset="utf-8">
<title>Pinecrest Mortgage Company – Stationery</title>
<link href="https://fonts.googleapis.com/css2?family=Josefin+Sans:wght@300;400;600&family=Arimo:wght@400;700&display=swap" rel="stylesheet">
<style>
  :root {
    --navy: #0f4d82;
    --sky: #0a89c9;
    --paper: #efefef;
    --backdrop: #e2e2e2;
    --ink: #1a1a1a;
    --grey-text: #6f6f6f;
    --light-on-navy: #dfe7ef;
  }
  * { box-sizing: border-box; margin: 0; padding: 0; }
  html, body { width: 1200px; height: 1167px; overflow: hidden; background: var(--backdrop); }
  body { position: relative; font-family: "Josefin Sans", sans-serif; }

  .piece { position: absolute; background: var(--paper); overflow: hidden; }
  .piece > svg.wave { position: absolute; inset: 0; width: 100%; height: 100%; }

  .wordmark {
    position: absolute; color: var(--navy); font-family: "Josefin Sans", sans-serif;
    font-weight: 600; text-transform: uppercase; line-height: 1; text-align: left;
  }
  .wordmark .line-main { display: block; letter-spacing: 0.01em; }
  .wordmark .line-sub { display: block; letter-spacing: 0.22em; margin-top: 4px; }

  /* Letterhead */
  .letterhead { left: 63px; top: 94px; width: 510px; height: 661px; }
  .letterhead .wordmark { left: 157px; top: 44px; }
  .letterhead .wordmark .line-main { font-size: 33px; }
  .letterhead .wordmark .line-sub { font-size: 9px; }
  .letter-meta { position: absolute; top: 174px; font-family: "Arimo", sans-serif; font-size: 8.5px; color: var(--grey-text); }
  .letter-meta strong { display: block; color: var(--ink); font-weight: 700; margin-bottom: 2px; }
  .letter-meta.subject { left: 148px; }
  .letter-meta.date { left: 418px; top: 172px; }
  .letter-sidebar { position: absolute; left: 20px; top: 279px; width: 89px; text-align: right; font-family: "Arimo", sans-serif; font-size: 8.3px; line-height: 12px; color: var(--grey-text); }
  .letter-sidebar p + p { margin-top: 3px; }
  .letter-sidebar .lead { color: var(--ink); }
  .letter-body { position: absolute; left: 148px; top: 227px; width: 314px; font-family: "Arimo", sans-serif; color: var(--grey-text); }
  .letter-body .salutation { font-size: 11px; margin-bottom: 12px; }
  .letter-body p.copy { font-size: 8.3px; line-height: 11px; text-align: justify; margin-bottom: 11px; }
  .letter-sign { position: absolute; left: 148px; top: 486px; font-family: "Arimo", sans-serif; font-size: 10.5px; line-height: 13px; color: var(--grey-text); }
  .letter-footer { position: absolute; left: 15px; top: 584px; color: var(--light-on-navy); font-size: 8.5px; line-height: 10.5px; font-weight: 300; }
  .letter-footer .contacts { margin-top: 6px; list-style: none; }
  .letter-footer .contacts li { display: flex; align-items: center; gap: 6px; }
  .dot { display: inline-block; border-radius: 50%; background: var(--sky); flex: none; }
  .letter-footer .dot { width: 6px; height: 6px; }

  /* Business cards */
  .card { width: 505px; height: 287px; border-radius: 25px; }
  .card-front { left: 628px; top: 111px; }
  .card-front .wordmark { left: 232px; top: 58px; }
  .card-front .wordmark .line-main { font-size: 40px; }
  .card-front .wordmark .line-sub { font-size: 11px; }
  .card-person { position: absolute; left: 21px; top: 157px; color: var(--light-on-navy); }
  .card-person .name { font-size: 17px; color: var(--sky); font-weight: 400; }
  .card-person .title { font-size: 13px; font-weight: 300; margin-top: 2px; }
  .card-contacts { position: absolute; left: 21px; top: 204px; list-style: none; color: var(--light-on-navy); font-size: 12px; font-weight: 300; line-height: 17px; }
  .card-contacts li { display: flex; align-items: center; gap: 6px; }
  .card-contacts .dot { width: 11px; height: 11px; }
  .card-address { position: absolute; right: 18px; top: 234px; text-align: right; color: var(--light-on-navy); font-size: 13px; font-weight: 300; line-height: 17px; }

  .card-back { left: 628px; top: 452px; background: var(--navy); }
  .card-back .wordmark { left: 0; right: 0; top: 112px; text-align: center; color: var(--light-on-navy); }
  .card-back .wordmark .line-main { font-size: 40px; }
  .card-back .wordmark .line-sub { font-size: 11px; }

  /* Envelopes */
  .envelope-front { left: 63px; top: 821px; width: 510px; height: 253px; }
  .envelope-front .wordmark { left: 318px; top: 44px; }
  .envelope-front .wordmark .line-main { font-size: 29px; }
  .envelope-front .wordmark .line-sub { font-size: 8px; }
  .envelope-return { position: absolute; left: 18px; top: 220px; color: var(--light-on-navy); font-size: 8px; line-height: 10px; font-weight: 300; }

  .envelope-back { left: 628px; top: 821px; width: 509px; height: 253px; }
  .envelope-back .wordmark { left: 0; right: 0; top: 26px; text-align: center; color: var(--light-on-navy); }
  .envelope-back .wordmark .line-main { font-size: 15px; }
  .envelope-back .wordmark .line-sub { font-size: 4.5px; margin-top: 2px; }
</style>
</head>
<body>

<section class="piece letterhead" aria-label="Letterhead">
  <svg class="wave" viewBox="0 0 510 661" preserveAspectRatio="none" aria-hidden="true">
    <path fill="var(--sky)" d="M0,575 C60,530 140,530 250,575 C340,612 420,635 470,610 C490,598 505,580 510,562 L510,661 L0,661 Z"/>
    <path fill="var(--navy)" stroke="#ffffff" stroke-width="0.8" d="M0,578 C70,545 150,550 250,592 C340,628 420,650 470,626 C490,614 505,586 510,562 L510,661 L0,661 Z"/>
  </svg>
  <div class="wordmark"><span class="line-main">Pinecrest</span><span class="line-sub">Mortgage Company</span></div>

  <div class="letter-meta subject"><strong>SUBJECT :</strong>Lorem Ipsum is simply dummy</div>
  <div class="letter-meta date"><strong>DATE :</strong>15-09-2017</div>

  <aside class="letter-sidebar">
    <p><span class="lead">Lorem Ipsum is</span><br>simply dummy text<br>of the printing</p>
    <p><span class="lead">Lorem Ipsum is</span><br>simply dummy text</p>
  </aside>

  <div class="letter-body">
    <p class="salutation">Dear Person,</p>
    <p class="copy">Lorem Ipsum is simply dummy text of the printing and typesetting industry. Lorem Ipsum has been the industry's standard dummy text ever since the 1500s, when an unknown printer took a galley of type and scrambled it to make a type specimen book. It has survived not only five centuries, but also the leap into electronic typesetting, remaining essentially unchanged. It was popularised in the 1960s with the release of Letraset sheets containing Lorem Ipsum passages, and more recently with desktop publishing software like Aldus PageMaker including versions of Lorem Ipsum.</p>
    <p class="copy">Lorem Ipsum is simply dummy text of the printing and typesetting industry. Lorem Ipsum has been the industry's standard dummy text ever since the 1500s, when an unknown printer took a galley of type and scrambled it to make a type specimen book. It has survived not only five centuries, but also the leap into electronic typesetting, remaining essentially unchanged. It was popularised in the 1960s with the release of</p>
    <p class="copy">Letraset sheets containing Lorem Ipsum passages, and more recently with desktop publishing software like Aldus PageMaker including versions of Lorem Ipsum.lease of Letraset sheets containing Lorem Ipsum passages, and more recently with desktop publishing software like Aldus PageMaker including versions of Lorem Ipsum. publishing software like Aldus PageMaker including versions of Lorem Ipsum.</p>
  </div>

  <div class="letter-sign">Owen Carter<br>Managing Director</div>

  <footer class="letter-footer">
    <p>NMLS 47162 - Company NMLS 61290<br>18 Larkin Ave, Seabrook Bay, SB 08614</p>
    <ul class="contacts">
      <li><span class="dot"></span>555-419-6253</li>
      <li><span class="dot"></span>888-304-2918</li>
      <li><span class="dot"></span>mhale@pinecrestmortgage.example</li>
      <li><span class="dot"></span>www.pinecrestmortgage.example</li>
    </ul>
  </footer>
</section>

<section class="piece card card-front" aria-label="Business card front">
  <svg class="wave" viewBox="0 0 505 287" preserveAspectRatio="none" aria-hidden="true">
    <path fill="var(--sky)" d="M0,127 C40,110 110,108 200,140 C280,170 330,205 380,210 C440,214 480,180 505,134 L505,287 L0,287 Z"/>
    <path fill="var(--navy)" stroke="#ffffff" stroke-width="0.8" d="M0,132 C45,116 115,118 200,152 C280,184 330,206 380,202 C440,196 480,170 505,134 L505,287 L0,287 Z"/>
  </svg>
  <div class="wordmark"><span class="line-main">Pinecrest</span><span class="line-sub">Mortgage Company</span></div>
  <div class="card-person">
    <p class="name">Marcus Hale</p>
    <p class="title">Vice President</p>
  </div>
  <ul class="card-contacts">
    <li><span class="dot"></span>555-419-6253</li>
    <li><span class="dot"></span>888-304-2918</li>
    <li><span class="dot"></span>mhale@pinecrestmortgage.example</li>
    <li><span class="dot"></span>www.pinecrestmortgage.example</li>
  </ul>
  <p class="card-address">NMLS 47162 - Company NMLS 61290<br>18 Larkin Ave, Seabrook Bay, SB 08614</p>
</section>

<section class="piece card card-back" aria-label="Business card back">
  <div class="wordmark"><span class="line-main">Pinecrest</span><span class="line-sub">Mortgage Company</span></div>
</section>

<section class="piece envelope-front" aria-label="Envelope front">
  <svg class="wave" viewBox="0 0 510 253" preserveAspectRatio="none" aria-hidden="true">
    <path fill="var(--sky)" d="M0,172 C40,148 100,140 190,168 C280,196 340,226 400,226 C450,226 490,200 510,168 L510,253 L0,253 Z"/>
    <path fill="var(--navy)" stroke="#ffffff" stroke-width="0.8" d="M0,175 C45,156 110,154 190,180 C280,210 340,232 400,230 C450,226 490,198 510,168 L510,253 L0,253 Z"/>
  </svg>
  <div class="wordmark"><span class="line-main">Pinecrest</span><span class="line-sub">Mortgage Company</span></div>
  <p class="envelope-return">NMLS 47162 - Company NMLS 61290<br>18 Larkin Ave, Seabrook Bay, SB 08614</p>
</section>

<section class="piece envelope-back" aria-label="Envelope back">
  <svg class="wave" viewBox="0 0 509 253" preserveAspectRatio="none" aria-hidden="true">
    <path fill="none" stroke="#d4d4d4" stroke-width="1" d="M14,45 L8,245 M495,45 L501,245"/>
    <path fill="var(--navy)" d="M0,0 H509 L493,45 Q490,55 478,57 L266,80 Q254,82 242,80 L31,57 Q19,55 16,45 Z"/>
  </svg>
  <div class="wordmark"><span class="line-main">Pinecrest</span><span class="line-sub">Mortgage Company</span></div>
</section>

</body>
</html>
```